Etiketten für Kürbiskernöl
Zielgruppe
Wir betreiben eine Landwirschaft, vorwiegend Ackerbau und Viehwirtschaft im nordöstlichen Niederösterreich. Wir sind ein reines Familienunternehmen. Unsere Zielgruppe ist 20 Jahre aufwärts, männlich wie weiblich und legt großen Wert auf Regionalität und hohe Qualität der Produkte.
Aufgabenstellung
Das Etikett wird für unsere Kürbiskernölflasche benötigt. Die Vorderseite soll unseren Namen, Produktbezeichnung und Füllmenge enthalten. Familie Wendtner - Kürbiskernöl 100% rein - 500ml Für die Rückseite gibt es einen entsprechenden Text (siehe Anhang).
Angehängt haben wir auch Etikett Vorderseiten, die uns sehr ansprechen. Es soll auf jeden Fall ein Kürbis abgebildet sein und ein hochwertiges, eher minimalistischen Design haben.
In Zukunft könnten wir uns auch vorstellen die Kürbiskerne in Form von Knabberkernen zu verkaufen, wofür wir das Etikettendesign gern abwandeln würden.
Farben: dunkelgrau/schwarz, weiß, dunkelgrün/oliv, beige
Flaschenform: Valmera 500ml siehe Foto

```html
<!DOCTYPE html>
<html lang="de">
<head>
<meta charset="utf-8">
<title>Kürbiskernöl – Etiketten Familie Wendtner</title>
<link rel="stylesheet" href="https://fonts.googleapis.com/css2?family=Amatic+SC:wght@400;700&family=Montserrat:wght@400;500;600&display=swap">
<style>
  :root {
    --canvas: #ffffff;
    --label: #1f1f1f;
    --ink: #f4f4f2;
    --ink-soft: #e6e6e3;
    --art-a: #3a3a38;
    --art-b: #262625;
  }
  * { margin: 0; padding: 0; box-sizing: border-box; }
  html, body {
    width: 1200px;
    height: 600px;
    overflow: hidden;
    background: var(--canvas);
  }
  .canvas {
    position: relative;
    width: 1200px;
    height: 600px;
  }
  .label {
    position: absolute;
    top: 32px;
    width: 238px;
    height: 536px;
    background: var(--label);
    color: var(--ink);
    font-family: "Montserrat", sans-serif;
  }
  .label--back { left: 343px; }
  .label--front { left: 619px; }

  .hand { font-family: "Amatic SC", cursive; font-weight: 400; }

  /* back label */
  .intro, .process {
    position: absolute;
    left: 22px;
    width: 200px;
    font-size: 9.2px;
    line-height: 11.4px;
    color: var(--ink-soft);
  }
  .intro { top: 26px; }
  .process { top: 115px; }
  .claim {
    position: absolute;
    top: 80px;
    left: 0;
    width: 238px;
    text-align: center;
    font-size: 16px;
    letter-spacing: 0.3px;
  }
  .address {
    position: absolute;
    top: 258px;
    left: 24px;
    font-size: 9.2px;
    line-height: 11.4px;
    color: var(--ink-soft);
  }
  .storage {
    position: absolute;
    top: 298px;
    left: 24px;
    font-size: 8px;
    color: var(--ink-soft);
  }
  .best-before {
    position: absolute;
    top: 316px;
    left: 24px;
    font-size: 8px;
    color: var(--ink-soft);
    display: flex;
    align-items: baseline;
    gap: 12px;
  }
  .best-before .date { font-size: 14px; color: var(--ink); }
  .art--back {
    position: absolute;
    left: 4px;
    top: 369px;
    width: 168px;
    height: 162px;
  }
  .volume {
    position: absolute;
    right: 16px;
    bottom: 10px;
    font-size: 22px;
    letter-spacing: 0.5px;
  }

  /* front label */
  .family {
    position: absolute;
    top: 20px;
    left: 0;
    width: 238px;
    text-align: center;
  }
  .family__prefix {
    display: block;
    font-size: 10px;
    font-weight: 500;
    letter-spacing: 4.5px;
    padding-left: 4.5px;
  }
  .family__name {
    display: block;
    font-size: 19px;
    letter-spacing: 1px;
    margin-top: 2px;
  }
  .product {
    position: absolute;
    top: 122px;
    left: 0;
    width: 238px;
    text-align: center;
    font-size: 64px;
    line-height: 64px;
    letter-spacing: 1px;
  }
  .purity {
    position: absolute;
    top: 275px;
    left: 0;
    width: 238px;
    text-align: center;
    font-size: 10px;
    font-weight: 500;
    letter-spacing: 4px;
    padding-left: 4px;
  }
  .art--front {
    position: absolute;
    left: 8px;
    top: 340px;
    width: 226px;
    height: 160px;
  }
  .method {
    position: absolute;
    bottom: 13px;
    left: 0;
    width: 238px;
    text-align: center;
    font-size: 8.4px;
    font-weight: 600;
    letter-spacing: 1.4px;
  }
</style>
</head>
<body>
<main class="canvas">

  <section class="label label--back" aria-label="Rückseitenetikett">
    <p class="intro">Nur die besten Kürbiskerne aus unserem eigenen Anbau werden zu unserem g'sund, g'schmackig, guatem Kürbiskernöl verarbeitet.</p>
    <p class="claim hand">100% rein und naturbelassen</p>
    <p class="process">Die Kürbiskerne werden schonend geröstet und in einem traditionellen Verfahren in einer regionalen Ölmühle kalt gepresst, was unserem Kürbiskernöl das einzigartige, intensiv-nussige Aroma verleiht.</p>
    <p class="address">Familie Wendtner<br>2071 Haselbach 38</p>
    <p class="storage">Vor Wärme und Licht geschützt lagern.</p>
    <p class="best-before"><span>Mindestens haltbar bis:</span><span class="date hand">Oktober 2022</span></p>
    <svg class="art--back" role="img" aria-label="Weiße Strichzeichnung eines Kürbisses, angeschnitten am linken Rand" viewBox="0 0 168 162">
      <defs>
        <radialGradient id="artBack" cx="50%" cy="55%" r="60%">
          <stop offset="0" stop-color="var(--art-a)"/>
          <stop offset="1" stop-color="var(--art-b)"/>
        </radialGradient>
      </defs>
      <rect width="168" height="162" rx="6" fill="url(#artBack)"/>
    </svg>
    <p class="volume hand">500 ml</p>
  </section>

  <section class="label label--front" aria-label="Vorderseitenetikett">
    <h2 class="family">
      <span class="family__prefix">FAMILIE</span>
      <span class="family__name hand">Wendtner</span>
    </h2>
    <h1 class="product hand">Kürbis<br>Kernöl</h1>
    <p class="purity">100% REIN</p>
    <svg class="art--front" role="img" aria-label="Weiße Strichzeichnung eines Kürbisses mit aufgeschnittenem Stück und Kernen" viewBox="0 0 226 160">
      <defs>
        <radialGradient id="artFront" cx="45%" cy="55%" r="60%">
          <stop offset="0" stop-color="var(--art-a)"/>
          <stop offset="1" stop-color="var(--art-b)"/>
        </radialGradient>
      </defs>
      <rect width="226" height="160" rx="6" fill="url(#artFront)"/>
    </svg>
    <p class="method">TRADITIONELL KALTGEPRESST</p>
  </section>

</main>
</body>
</html>
```